TRVesper Labels*

We are in the cannabis industry selling Cannabis products in a 1oz jar, 3oz jar and 7 oz jars. we have pre-rolls too.

We need various sizes logo label stickers for small jars and tubes. I need label sticker designs for some 1"x2", 2"x3", 2"x2" stickers logo. See attached for examples.

I'm attaching some samples for you to look at and see if you can design something in similar.

Attached is our Logo designed my PixelHarbor Project Design #: 58402936
Our Slogan is:

“Staying Passionate and motivated with Small Batch Harvests”

For any questions please do not hesitate to ask. Thank you

Target Market(s)

general comsumers

Industry/Entity Type

Cannabis

Font styles to use
Decorative

Colors
abd037
f36f22
f78f20
ffc41a

Requirements
Must have
• Warning: This product may be unlawful outside of the State of Washington. This soil grown product has intoxicating effects and my be habit forming. Smoking is hazardous to your health. There may be health risks associated with the consumption of this product. Marijuana can impair concentration, coordination and judgement. Do not operate a vehicle or machinery under the influence of this drug. Should not be use by women that are pregnant or breast feeding. For use only by adults twenty-one and older. Keep out reach of children.
Nice to have
• Small text box for cannabis name and strain type
• Marketing: Check Us Out!
• www.TRVesperLLC-example.com
• TRVesperLLC@mailbox-example.com
• Chatterbook TRVesper LLC

```html
<!DOCTYPE html>
<html lang="en">
<head>
<meta charset="utf-8">
<title>TRVesper Jar Labels</title>
<link rel="stylesheet" href="https://fonts.googleapis.com/css2?family=Quicksand:wght@600&family=Arimo:wght@400&display=swap">
<style>
  :root {
    --page: #ffffff;
    --forest-deep: #062a0b;
    --forest: #0f4416;
    --brand-green: #a6d13a;
    --ink-light: #ffffff;
    --ink-dark: #1b1b1b;
    --warning-red: #ff2a2a;
    --gold-edge: #c4702a;
    --gold-mid: #f2c91e;
    --gold-bright: #fff04a;
    --olive-band: #4e7a1c;
    --grass-band: #14a52c;
    --grass-glow: #45c94e;
  }
  * { box-sizing: border-box; margin: 0; padding: 0; }
  html, body { width: 1200px; height: 1200px; overflow: hidden; background: var(--page); }
  body { position: relative; font-family: "Arimo", Arial, sans-serif; }

  .label {
    position: absolute;
    left: 177px;
    width: 874px;
    height: 277px;
    overflow: hidden;
  }
  .label--gold  { top: 153px; }
  .label--olive { top: 458px; }
  .label--grass { top: 770px; left: 178px; }

  .label__field {
    position: absolute;
    inset: 0 0 62px 0;
    background:
      radial-gradient(ellipse 30% 90% at 50% 40%, rgba(70,150,40,.35), transparent 70%),
      linear-gradient(180deg, var(--forest) 0%, var(--forest-deep) 100%);
  }
  .label--olive .label__field,
  .label--grass .label__field {
    background:
      linear-gradient(90deg, transparent 33%, rgba(90,190,50,.25) 35%, transparent 38%, transparent 47%, rgba(120,210,60,.3) 50%, transparent 53%, transparent 61%, rgba(90,190,50,.2) 63%, transparent 66%),
      radial-gradient(ellipse 30% 90% at 50% 40%, rgba(70,150,40,.35), transparent 70%),
      linear-gradient(180deg, var(--forest) 0%, var(--forest-deep) 100%);
  }

  .brand {
    position: absolute;
    transform: translateX(-50%);
    display: flex;
    flex-direction: column;
    align-items: center;
    font-family: "Quicksand", "Trebuchet MS", sans-serif;
    font-weight: 600;
    color: var(--brand-green);
    line-height: 1;
    white-space: nowrap;
  }
  .brand__dot {
    border-radius: 50%;
    background: var(--brand-green);
    margin-bottom: 8px;
  }
  .brand--side { font-size: 26px; top: 50px; }
  .brand--side .brand__dot { width: 34px; height: 34px; }
  .brand--left  { left: 116px; }
  .brand--right { left: 617px; top: 54px; }
  .brand--main { left: 429px; top: 52px; font-size: 36px; }
  .brand--main .brand__dot { width: 52px; height: 52px; margin-bottom: 10px; }

  .product-spec {
    position: absolute;
    left: 22px;
    top: 160px;
    width: 254px;
    list-style: none;
    color: var(--ink-light);
    font-size: 11.5px;
    line-height: 15.5px;
  }
  .product-spec li { display: flex; align-items: baseline; }
  .product-spec .leader { flex: 1; border-bottom: 1px dotted rgba(255,255,255,.8); margin: 0 1px 3px; }

  .slogan {
    position: absolute;
    left: 429px;
    top: 161px;
    transform: translateX(-50%);
    color: var(--ink-light);
    font-size: 15.5px;
    letter-spacing: .06em;
    white-space: nowrap;
  }
  .slogan-sub {
    position: absolute;
    left: 429px;
    top: 192px;
    transform: translateX(-50%);
    color: var(--ink-light);
    font-size: 11px;
    letter-spacing: .03em;
    white-space: nowrap;
  }

  .compliance-mark {
    position: absolute;
    left: 806px;
    top: 72px;
    width: 44px;
    height: 44px;
  }

  .warning {
    position: absolute;
    left: 569px;
    top: 146px;
    width: 275px;
    color: var(--ink-light);
    font-size: 6.7px;
    line-height: 10px;
    text-align: justify;
  }
  .warning__lead { color: var(--warning-red); }

  .band {
    position: absolute;
    left: 0; right: 0; bottom: 0;
    height: 62px;
    font-size: 12px;
  }
  .label--gold .band {
    background: linear-gradient(90deg, var(--gold-edge) 0%, var(--gold-mid) 22%, var(--gold-bright) 45%, var(--gold-mid) 70%, var(--gold-edge) 100%);
    color: var(--ink-dark);
  }
  .label--olive .band {
    background:
      linear-gradient(90deg, transparent 33%, rgba(140,220,60,.55) 35%, transparent 38%, transparent 48%, rgba(150,230,70,.6) 50%, transparent 53%),
      var(--olive-band);
    border-top: 3px solid var(--gold-mid);
    color: var(--ink-light);
  }
  .label--grass .band {
    background: linear-gradient(90deg, var(--grass-band) 0%, var(--grass-glow) 50%, var(--grass-band) 100%);
    border-top: 2px solid #d6f0d0;
    color: var(--ink-light);
  }

  .band__marketing { position: absolute; left: 15px; top: 10px; line-height: 16px; }
  .band__marketing .addr { font-size: 12.5px; }
  .band__center {
    position: absolute;
    left: 429px;
    top: 10px;
    transform: translateX(-50%);
    text-align: center;
    font-size: 10.5px;
    line-height: 13px;
    white-space: nowrap;
  }
  .band__center .netwt { font-size: 9.5px; margin-bottom: 4px; }
  .band__contacts {
    position: absolute;
    left: 575px;
    top: 10px;
    list-style: none;
    font-size: 11px;
    line-height: 14.5px;
  }
  .band__contacts li { display: flex; align-items: center; gap: 6px; }
  .band__contacts svg { width: 12px; height: 12px; flex: none; }
  .social-dot { width: 10px; height: 10px; border-radius: 50%; background: #2a5fc4; margin: 0 1px; flex: none; }
</style>
</head>
<body>

<!-- Label A: gold band -->
<section class="label label--gold">
  <div class="label__field" role="img" aria-label="Deep green backdrop with a faint repeating leaf and brand-name pattern"></div>
  <div class="brand brand--side brand--left"><span class="brand__dot"></span>TRVesper</div>
  <div class="brand brand--main"><span class="brand__dot"></span>TRVesper</div>
  <div class="brand brand--side brand--right"><span class="brand__dot"></span>TRVesper</div>
  <svg class="compliance-mark" viewBox="0 0 44 44" aria-hidden="true"><path d="M22 3 L41 38 H3 Z" fill="none" stroke="#fff" stroke-width="3" stroke-linejoin="round"/></svg>
  <ul class="product-spec">
    <li>Type<span class="leader"></span>Flower</li>
    <li>Strain<span class="leader"></span>NW.Cedar&nbsp;&nbsp;Haze</li>
    <li>NetWeight<span class="leader"></span>3.5 grams</li>
  </ul>
  <p class="slogan">Growing Patient &amp; Dedicated</p>
  <p class="slogan-sub">with Small Batch Harvests</p>
  <p class="warning"><span class="warning__lead">WARNING:</span> This product may be unlawful outside of the State of Washington. This soil grown product has intoxicating effects and my be habit forming. Smoking is hazardous to your health. There may be health risks associated with the consumption of this product. Marijuana can impair concentration, coordination and judgement. Do not operate a vehicle or machinery under the influence of this drug. Should not be use by women that are pregnant or breast feeding. For use only by adults twenty-one and older. Keep out reach of children.</p>
  <div class="band">
    <div class="band__marketing">Marketing:<br><span class="addr">1450 Example Ave S, Seattle, WA 98100</span></div>
    <div class="band__center"><div class="netwt">NET WT&nbsp;&nbsp;(300G)</div>Visit us at:<br>www.TRVesperLLC-example.com</div>
    <ul class="band__contacts">
      <li><svg viewBox="0 0 12 12"><circle cx="6" cy="6" r="5.3" fill="none" stroke="currentColor"/><path d="M4 3.2 5 4.6 4.5 5.3q.8 1.5 2.2 2.2l.7-.5 1.4 1-.6 1q-2.6-.3-4.3-3.8z" fill="currentColor"/></svg>(206) 555-0142</li>
      <li><svg viewBox="0 0 12 12"><rect x="1" y="2.5" width="10" height="7" fill="currentColor"/><path d="M1 2.5 6 6.5 11 2.5" fill="none" stroke="#f2c91e" stroke-width=".9"/></svg>TRVesperLLC@mailbox-example.com</li>
      <li><span class="social-dot"></span>Chatterbook TRVesper LLC</li>
    </ul>
  </div>
</section>

<!-- Label B: olive band -->
<section class="label label--olive">
  <div class="label__field" role="img" aria-label="Deep green backdrop with light streaks and a faint repeating leaf and brand-name pattern"></div>
  <div class="brand brand--side brand--left"><span class="brand__dot"></span>TRVesper</div>
  <div class="brand brand--main"><span class="brand__dot"></span>TRVesper</div>
  <div class="brand brand--side brand--right"><span class="brand__dot"></span>TRVesper</div>
  <svg class="compliance-mark" viewBox="0 0 44 44" aria-hidden="true"><path d="M22 3 L41 38 H3 Z" fill="none" stroke="#fff" stroke-width="3" stroke-linejoin="round"/></svg>
  <ul class="product-spec">
    <li>Type<span class="leader"></span>Flower</li>
    <li>Strain<span class="leader"></span>NW.Cedar&nbsp;&nbsp;Haze</li>
    <li>NetWeight<span class="leader"></span>3.5 grams</li>
  </ul>
  <p class="slogan">Growing Patient &amp; Dedicated</p>
  <p class="slogan-sub">with Small Batch Harvests</p>
  <p class="warning"><span class="warning__lead">WARNING:</span> This product may be unlawful outside of the State of Washington. This soil grown product has intoxicating effects and my be habit forming. Smoking is hazardous to your health. There may be health risks associated with the consumption of this product. Marijuana can impair concentration, coordination and judgement. Do not operate a vehicle or machinery under the influence of this drug. Should not be use by women that are pregnant or breast feeding. For use only by adults twenty-one and older. Keep out reach of children.</p>
  <div class="band">
    <div class="band__marketing">Marketing:<br><span class="addr">1450 Example Ave S, Seattle, WA 98100</span></div>
    <div class="band__center"><div class="netwt">NET WT&nbsp;&nbsp;(300G)</div>Visit us at:<br>www.TRVesperLLC-example.com</div>
    <ul class="band__contacts">
      <li><svg viewBox="0 0 12 12"><circle cx="6" cy="6" r="5.3" fill="none" stroke="currentColor"/><path d="M4 3.2 5 4.6 4.5 5.3q.8 1.5 2.2 2.2l.7-.5 1.4 1-.6 1q-2.6-.3-4.3-3.8z" fill="currentColor"/></svg>(206) 555-0142</li>
      <li><svg viewBox="0 0 12 12"><rect x="1" y="2.5" width="10" height="7" fill="currentColor"/><path d="M1 2.5 6 6.5 11 2.5" fill="none" stroke="#4e7a1c" stroke-width=".9"/></svg>TRVesperLLC@mailbox-example.com</li>
      <li><span class="social-dot"></span>Chatterbook TRVesper LLC</li>
    </ul>
  </div>
</section>

<!-- Label C: grass-green band -->
<section class="label label--grass">
  <div class="label__field" role="img" aria-label="Deep green backdrop with light streaks and a faint repeating leaf and brand-name pattern"></div>
  <div class="brand brand--side brand--left"><span class="brand__dot"></span>TRVesper</div>
  <div class="brand brand--main"><span class="brand__dot"></span>TRVesper</div>
  <div class="brand brand--side brand--right"><span class="brand__dot"></span>TRVesper</div>
  <svg class="compliance-mark" viewBox="0 0 44 44" aria-hidden="true"><path d="M22 3 L41 38 H3 Z" fill="none" stroke="#fff" stroke-width="3" stroke-linejoin="round"/></svg>
  <ul class="product-spec">
    <li>Type<span class="leader"></span>Flower</li>
    <li>Strain<span class="leader"></span>NW.Cedar&nbsp;&nbsp;Haze</li>
    <li>NetWeight<span class="leader"></span>3.5 grams</li>
  </ul>
  <p class="slogan">Growing Patient &amp; Dedicated</p>
  <p class="slogan-sub">with Small Batch Harvests</p>
  <p class="warning"><span class="warning__lead">WARNING:</span> This product may be unlawful outside of the State of Washington. This soil grown product has intoxicating effects and my be habit forming. Smoking is hazardous to your health. There may be health risks associated with the consumption of this product. Marijuana can impair concentration, coordination and judgement. Do not operate a vehicle or machinery under the influence of this drug. Should not be use by women that are pregnant or breast feeding. For use only by adults twenty-one and older. Keep out reach of children.</p>
  <div class="band">
    <div class="band__marketing">Marketing:<br><span class="addr">1450 Example Ave S, Seattle, WA 98100</span></div>
    <div class="band__center"><div class="netwt">NET WT&nbsp;&nbsp;(300G)</div>Visit us at:<br>www.TRVesperLLC-example.com</div>
    <ul class="band__contacts">
      <li><svg viewBox="0 0 12 12"><circle cx="6" cy="6" r="5.3" fill="none" stroke="currentColor"/><path d="M4 3.2 5 4.6 4.5 5.3q.8 1.5 2.2 2.2l.7-.5 1.4 1-.6 1q-2.6-.3-4.3-3.8z" fill="currentColor"/></svg>(206) 555-0142</li>
      <li><svg viewBox="0 0 12 12"><rect x="1" y="2.5" width="10" height="7" fill="currentColor"/><path d="M1 2.5 6 6.5 11 2.5" fill="none" stroke="#14a52c" stroke-width=".9"/></svg>TRVesperLLC@mailbox-example.com</li>
      <li><span class="social-dot"></span>Chatterbook TRVesper LLC</li>
    </ul>
  </div>
</section>

</body>
</html>
```